SOLVEN TRIDE PORTAL

I'D LIKE TO REDESIGN MY WEBSITE TO MATCH WITH THE NEW BROCHURE WHICH IS ATTACHED. CONTENT AND LOGOS ARE ATTACHED. PLEASE USE WATCH BRAND LOGOS FROM THE BROCHURE
Coded - Design and coding required
1 page

```html
<!DOCTYPE html>
<html lang="en">
<head>
<meta charset="utf-8">
<title>Solven Tride Portal</title>
<link href="https://fonts.googleapis.com/css2?family=Marcellus&family=Kurale&family=Poppins:wght@400;600&display=swap" rel="stylesheet">
<style>
:root{
  --black:#000;
  --ink:#0b0b0b;
  --topbar:#a6a6a6;
  --about-bg:#3b3b3b;
  --invest-bg:#1c1c1c;
  --source-bg:#121212;
  --field:#232323;
  --white:#fff;
  --text:#e6e6e6;
  --muted:#a9a9a9;
  --heading-grey:#cfcfcf;
  --line:#555;
}
*{box-sizing:border-box;margin:0;padding:0}
html,body{width:1200px;height:2548px;overflow:hidden;background:var(--black)}
body{font-family:"Kurale",serif;color:var(--text)}
.page{position:relative;width:1200px;height:2548px;overflow:hidden}
section,header,footer{position:absolute;left:0;width:1200px}
.abs{position:absolute}

/* header */
.topbar{top:0;height:40px;background:var(--topbar);font-family:"Poppins",sans-serif;font-size:9.5px;color:#111}
.topbar .contact-item{position:absolute;top:14px;display:flex;align-items:center;gap:7px}
.topbar .contact-item b{font-weight:600}
.topbar .divider{position:absolute;top:11px;width:1px;height:18px;background:#666}
.social{position:absolute;top:11px;left:1019px;display:flex;gap:7px}
.social span{width:18px;height:18px;border-radius:50%;background:#111;display:block}
.navbar{top:40px;height:81px;background:var(--black)}
.brand{position:absolute;left:104px;top:0;width:157px;height:121px;background:var(--ink);z-index:2;display:flex;flex-direction:column;align-items:center;justify-content:center;gap:8px}
.brand .mark{width:22px;height:22px;border:1px solid #cfcfcf}
.brand .name{font-family:"Marcellus",serif;font-size:13px;color:#e4e4e4;letter-spacing:.5px;text-align:center;line-height:1.2}
.nav{position:absolute;right:104px;top:35px;display:flex;gap:26px;font-family:"Poppins",sans-serif;font-size:10.5px;color:var(--white)}
.nav a{color:inherit;text-decoration:none;position:relative}
.nav a.active::after{content:"";position:absolute;left:0;right:0;top:40px;height:1px;background:var(--white)}

/* hero */
.hero{top:121px;height:537px;background:radial-gradient(ellipse at 70% 40%,#3a3a3a 0%,#262626 45%,#161616 100%)}
.hero-title{top:118px;width:100%;text-align:center;font-family:"Marcellus",serif;font-size:40px;line-height:53px;color:var(--white);font-weight:400}
.hero-copy{top:245px;left:215px;width:770px;text-align:center;font-size:12.5px;line-height:20.5px;color:var(--muted)}
.hero-copy p+p{margin-top:13px}
.btn{position:absolute;display:flex;align-items:center;justify-content:center;border:2px solid var(--white);border-radius:22px;color:var(--white);font-family:"Kurale",serif;text-decoration:none}
.hero .btn{left:517px;top:388px;width:164px;height:41px;font-size:18px;color:#cfcfcf}

/* about */
.about{top:658px;height:497px;background:linear-gradient(135deg,#444 0%,#393939 50%,#2f2f2f 100%)}
.about-photo{left:105px;top:64px;width:459px;height:328px;background:linear-gradient(135deg,#1b1b1b 0%,#8a8a8a 45%,#bdbdbd 60%,#2a2a2a 100%)}
.section-title{font-family:"Marcellus",serif;font-weight:400;color:var(--heading-grey)}
.about h2{left:600px;top:62px;font-size:38px}
.about-copy{left:601px;top:125px;width:494px;font-size:11.5px;line-height:21px;color:#e8e8e8}
.about-copy p+p{margin-top:15px}
.about .btn{left:600px;top:413px;width:155px;height:37px;font-size:14px}

/* investments */
.investments{top:1155px;height:257px;background:var(--invest-bg);text-align:center}
.investments h2{top:60px;width:100%;font-size:38px}
.investments .lead{top:128px;width:100%;font-size:16.5px;color:#e2e2e2}
.investments .note{top:171px;width:100%;font-size:12px;color:#e2e2e2}

/* sourcing */
.sourcing{top:1412px;height:623px;background:var(--source-bg)}
.sourcing h2{top:62px;width:100%;text-align:center;font-size:38px}
.sourcing .lead{top:141px;left:330px;width:540px;text-align:center;font-size:12.5px;line-height:23px;color:#e8e8e8}
.field{position:absolute;background:var(--field);border-radius:3px;font-size:8.5px;letter-spacing:.3px;color:#a0a0a0;padding:16px 0 0 16px;text-transform:uppercase}
.sourcing .btn{left:525px;top:551px;width:154px;height:36px;font-size:14px}

/* contact */
.contact{top:2035px;height:436px;background:var(--black)}
.contact-brand{left:471px;top:70px;width:104px;display:flex;flex-direction:column;align-items:center;gap:6px}
.contact-brand .mark{width:20px;height:20px;border:1px solid #cfcfcf}
.contact-brand .name{font-family:"Marcellus",serif;font-size:10px;color:#e4e4e4;text-align:center;line-height:1.2}
.contact-line{right:622px;font-size:12px;color:#eee;text-align:right;display:flex;align-items:center;gap:9px}
.contact-line.icon-gap{right:626px}
.address{right:654px;top:255px;text-align:right;font-size:12px;line-height:18px;color:#eee}
.alt-note{right:619px;top:307px;text-align:right;font-size:12px;line-height:18px;color:#eee}
.alt-note span{color:var(--muted);font-size:13px}
.contact .btn{left:616px;top:344px;width:154px;height:36px;font-size:14px}

/* bottom */
.bottombar{top:2471px;height:77px;background:var(--black);border-top:1px solid #222}
.copyright{left:105px;top:34px;font-size:10.5px;color:#bbb}
.footer-nav{right:105px;top:34px;font-size:9.5px;color:#999;display:flex;gap:10px}
.footer-nav i{font-style:normal;color:#777}
</style>
</head>
<body>
<div class="page">

<header>
  <div class="abs topbar" style="position:absolute;left:0;width:1200px">
    <div class="contact-item" style="left:561px">
      <svg width="12" height="11" viewBox="0 0 12 11"><path d="M1 3c0-1.5 2-2.5 5-2.5S11 1.5 11 3v1H8.5V2.8h-5V4H1z M3 5h6l1.5 5h-9z" fill="none" stroke="#222" stroke-width="1"/><circle cx="6" cy="7.5" r="1.3" fill="none" stroke="#222"/></svg>
      <span><b>Need Help? Call Us! 01614407219</b></span>
    </div>
    <span class="divider" style="left:754px"></span>
    <div class="contact-item" style="left:786px">
      <svg width="13" height="10" viewBox="0 0 13 10"><rect x=".5" y=".5" width="12" height="9" fill="none" stroke="#222"/><path d="M.5 .5l6 5 6-5" fill="none" stroke="#222"/></svg>
      <span><b>Email:</b> Sales@solventride-portal.co.uk</span>
    </div>
    <span class="divider" style="left:1007px"></span>
    <div class="social" aria-label="Social links"><span></span><span></span><span></span></div>
  </div>
  <div class="abs navbar" style="position:absolute;left:0;width:1200px;top:40px">
    <nav class="nav">
      <a class="active" href="#">HOME</a>
      <a href="#">ABOUT</a>
      <a href="#">INVESTMENTS</a>
      <a href="#">SEARCH WATCHES</a>
      <a href="#">CONTACT</a>
    </nav>
  </div>
  <div class="brand">
    <span class="mark"></span>
    <span class="name">SOLVEN TRIDE<br>PORTAL</span>
  </div>
</header>

<section class="hero" role="img" aria-label="Dark close-up photograph of luxury wristwatches">
  <h1 class="abs hero-title">Welcome to Solven Tride Portal<br>International luxury timepiece supplier</h1>
  <div class="abs hero-copy">
    <p>Simply choose a desired product and allow us to source it for you at the best price and with suitable delivery terms. You will have an option to either collect your purchase from our Cheshire based boutique store, collection points are also in New York City or Dubai or get it delivered to your door via one of our fully insured couriers.</p>
    <p>Making your luxury shopping experience as simple as it can be.</p>
  </div>
  <a class="btn" href="#">ENQUIRE</a>
</section>

<section class="about">
  <div class="abs about-photo" role="img" aria-label="Photograph of two steel chronograph wristwatches held in hand"></div>
  <h2 class="abs section-title">About us</h2>
  <div class="abs about-copy">
    <p>Solven Tride Portal was first founded in 2018, it has been established as the premier resource to buy and sell premium pre-owned watches. With thousands of watches available from brands including Valcour, Orsenne Brach, Halbrecht, Marlowe Kiel, Tessaro, Delacourt and more, plus international locations and clients there’s no better place to find a luxury timepiece.</p>
    <p>Outstanding customer service is a mainstay of the Solven Tride ethos. Watch collectors are discerning shoppers, and will accept nothing but the best, which is why customer service has and always will be such an important part of the business.</p>
    <p>Our dedicated team of swiss watch experts are perfectly placed to adapt to the ever changing market conditions, giving our investors an ‘out of the box’ solution. Longevity is as much a focus as immediate success, ensuring you have the best options we can provide tomorrow as well as today.</p>
  </div>
  <a class="btn" href="#">GET IN TOUCH</a>
</section>

<section class="investments">
  <h2 class="abs section-title">Investments</h2>
  <p class="abs lead">Interested in becoming part of the ever growing Solven Tride Portal?</p>
  <p class="abs note">Please leave your details contact form below and one of the team will be in touch to discuss potential options.</p>
</section>

<section class="sourcing">
  <h2 class="abs section-title">Sourcing your watch</h2>
  <p class="abs lead">Complete the form below and a member of our team will be in contact to help you explore our range of high-end timepieces.</p>
  <div class="field" style="left:255px;top:212px;width:333px;height:40px">Watch brand</div>
  <div class="field" style="left:612px;top:212px;width:333px;height:40px">Year</div>
  <div class="field" style="left:255px;top:273px;width:333px;height:40px">Material</div>
  <div class="field" style="left:612px;top:273px;width:333px;height:40px">Bezel</div>
  <div class="field" style="left:255px;top:334px;width:333px;height:40px">Strap</div>
  <div class="field" style="left:612px;top:334px;width:333px;height:40px"></div>
  <span class="abs" style="left:628px;top:382px;font-size:8.5px;color:#a0a0a0">DIAL COLOUR</span>
  <div class="field" style="left:255px;top:396px;width:688px;height:109px">Message</div>
  <a class="btn" href="#">SUBMIT</a>
</section>

<section class="contact">
  <div class="abs contact-brand">
    <span class="mark"></span>
    <span class="name">SOLVEN TRIDE<br>PORTAL</span>
  </div>
  <div class="abs contact-line" style="top:183px">01614407219
    <svg width="18" height="18" viewBox="0 0 18 18"><path d="M4 2l3 3-1.5 2c1 2 3 4 5 5l2-1.5 3 3-2 2C8 15 3 10 2 4z" fill="none" stroke="#ddd" stroke-width="1.4"/></svg>
  </div>
  <div class="abs contact-line" style="top:208px">Sales@solventride-portal.co.uk
    <svg width="18" height="13" viewBox="0 0 18 13"><rect x=".7" y=".7" width="16.6" height="11.6" fill="none" stroke="#ddd" stroke-width="1.4"/><path d="M.7 .7l8.3 6.5 8.3-6.5" fill="none" stroke="#ddd" stroke-width="1.4"/></svg>
  </div>
  <p class="abs address">27 Mill Row, Harwick,<br>Calderton CK4 9LP, United Kingdom</p>
  <p class="abs alt-note">Alternatively please feel free to contact us on <span>01614407219</span><br>For a more detailed chat with one of our timepiece specialists</p>
  <div class="field" style="left:618px;top:69px;width:333px;height:40px">Watch brand</div>
  <div class="field" style="left:618px;top:125px;width:333px;height:40px">Watch brand</div>
  <div class="field" style="left:618px;top:180px;width:159px;height:40px">Phone number</div>
  <div class="field" style="left:792px;top:180px;width:159px;height:40px">Email</div>
  <div class="field" style="left:618px;top:235px;width:333px;height:78px">Message</div>
  <a class="btn" href="#">SUBMIT</a>
</section>

<footer class="bottombar">
  <p class="abs copyright">© 2022 Solven Tride Portal. All Rights Reserved.</p>
  <nav class="abs footer-nav">
    <span>HOME</span><i>|</i><span>ABOUT</span><i>|</i><span>INVESTMENTS</span><i>|</i><span>SEARCH WATCHES</span><i>|</i><span>CONTACT</span>
  </nav>
</footer>

</div>
</body>
</html>
```